Duck Call Company Business Card / Stationary
R7 Calls
Use same font as used in my logo
Dale Mertin
Owner
4816 North Belvin Rd.
Reedport, LA 70455
mertinsflightgear@pondmail.net
www.mertinsflightgear.net

```html
<!DOCTYPE html>
<html lang="en">
<head>
<meta charset="utf-8">
<title>R7 Calls — Business Card</title>
<link rel="stylesheet" href="https://fonts.googleapis.com/css2?family=Open+Sans:wght@400;600&display=swap">
<style>
  :root {
    --backdrop: #e9e6e2;
    --card: #ffffff;
    --band-dark: #5b4641;
    --band-light: #c9c4c1;
    --ink: #3d3431;
    --ink-soft: #6d6462;
    --rule: #b9b2ae;
    --icon: #5b4641;
  }
  * { box-sizing: border-box; margin: 0; padding: 0; }
  html, body {
    width: 1200px;
    height: 914px;
    overflow: hidden;
    background: var(--backdrop);
    font-family: "Open Sans", Arial, sans-serif;
  }
  .card {
    position: absolute;
    left: 100px;
    top: 171px;
    width: 1000px;
    height: 572px;
    background: var(--card);
    box-shadow: 0 10px 30px rgba(0,0,0,0.12);
    overflow: hidden;
  }
  .brand {
    position: absolute;
    left: 150px;
    top: 170px;
    width: 300px;
    height: 200px;
    display: flex;
    align-items: center;
    justify-content: center;
    gap: 18px;
  }
  .brand-dot {
    width: 44px;
    height: 44px;
    border-radius: 50%;
    background: var(--band-dark);
  }
  .brand-name {
    font-size: 44px;
    font-weight: 600;
    color: var(--band-dark);
    letter-spacing: 1px;
  }
  .divider {
    position: absolute;
    left: 478px;
    top: 160px;
    width: 1px;
    height: 230px;
    background: var(--rule);
  }
  .contact {
    position: absolute;
    left: 502px;
    top: 168px;
    color: var(--ink);
  }
  .contact-name {
    font-size: 24px;
    font-weight: 600;
    line-height: 1.15;
  }
  .contact-role {
    font-size: 16px;
    color: var(--ink-soft);
    margin-bottom: 22px;
  }
  .contact-list { list-style: none; }
  .contact-list li {
    display: flex;
    align-items: flex-start;
    gap: 10px;
    font-size: 16px;
    line-height: 1.35;
    margin-bottom: 6px;
  }
  .contact-list svg {
    flex: none;
    width: 18px;
    height: 18px;
    margin-top: 2px;
  }
  .band {
    position: absolute;
    left: 0;
    bottom: 0;
    width: 100%;
    height: 34px;
  }
</style>
</head>
<body>
  <div class="card">
    <div class="brand">
      <span class="brand-dot"></span>
      <span class="brand-name">R7 Calls</span>
    </div>

    <div class="divider"></div>

    <div class="contact">
      <p class="contact-name">Dale Mertin</p>
      <p class="contact-role">Owner</p>
      <ul class="contact-list">
        <li>
          <svg viewBox="0 0 18 18"><circle cx="9" cy="9" r="9" fill="var(--icon)"/><path d="M9 4a3.2 3.2 0 0 0-3.2 3.2C5.8 9.6 9 13.5 9 13.5s3.2-3.9 3.2-6.3A3.2 3.2 0 0 0 9 4zm0 4.4a1.2 1.2 0 1 1 0-2.4 1.2 1.2 0 0 1 0 2.4z" fill="#fff"/></svg>
          <span>4816 North Belvin Rd.<br>Reedport, LA 70455</span>
        </li>
        <li>
          <svg viewBox="0 0 18 18"><circle cx="9" cy="9" r="9" fill="var(--icon)"/><path d="M6.2 4.6l1.5-.3.9 2.2-1 .8a6 6 0 0 0 2.4 2.4l.8-1 2.2.9-.3 1.5c-.1.4-.5.7-.9.6A7.4 7.4 0 0 1 5.6 5.5c0-.4.2-.8.6-.9z" fill="#fff"/></svg>
          <span>555.555.0148</span>
        </li>
        <li>
          <svg viewBox="0 0 18 18"><circle cx="9" cy="9" r="9" fill="var(--icon)"/><rect x="4.5" y="5.8" width="9" height="6.4" rx="0.8" fill="#fff"/><path d="M4.8 6.2L9 9.4l4.2-3.2" fill="none" stroke="var(--icon)" stroke-width="0.9"/></svg>
          <span>mertinsflightgear@pondmail.net</span>
        </li>
        <li>
          <svg viewBox="0 0 18 18"><circle cx="9" cy="9" r="9" fill="var(--icon)"/><circle cx="9" cy="9" r="4.3" fill="none" stroke="#fff" stroke-width="1"/><path d="M4.7 9h8.6M9 4.7c-2 2.4-2 6.2 0 8.6M9 4.7c2 2.4 2 6.2 0 8.6" fill="none" stroke="#fff" stroke-width="0.8"/></svg>
          <span>www.mertinsflightgear.net</span>
        </li>
      </ul>
    </div>

    <svg class="band" viewBox="0 0 1000 34" preserveAspectRatio="none" aria-hidden="true">
      <rect x="0" y="0" width="1000" height="34" fill="var(--band-light)"/>
      <polygon points="0,0 520,0 548,34 0,34" fill="var(--band-dark)"/>
    </svg>
  </div>
</body>
</html>
```